Deodorant Product Sales One Pager and Annexes

Schedule: Very short deadline - to be complete within 12 hours
Budget: 2-3 hours
Format: Adobe Illustrator / A4 landscape or portrait - for submission by email in PDF
OBJECTIVE
We need a one pager sales sheet and its annexes to present a new deodorant range to the largest supermarket chain in Australia. This is a very important submission that can create more design projects for you. Please refer to the attachments for a starting point. We need to keep the design minimalist and elegant, stylish, clean and chic IN KEEPING WITH THE 1.618 ratio. Styles to avoid are too bright colors, clutter, comic or gimmicky styles. Please maintain a sense of high quality design and professionalism as this is a premium product in Australia.
TARGET AUDIENCE
Senior buyer of largest supermarket chain in Australia
Target Market(s)
Senior cosmetics buyer at Australia's largest supermarket chain

```html
<!DOCTYPE html>
<html lang="en">
<head>
<meta charset="utf-8">
<title>The Aluminium Free Deodorant Trend</title>
<link href="https://fonts.googleapis.com/css2?family=Bitter:ital,wght@0,400;0,600;0,700;1,400;1,600;1,700&family=Roboto:wght@400;500&display=swap" rel="stylesheet">
<style>
  :root {
    --page: #ffffff;
    --ink-dark: #2f3a44;
    --ink-mid: #5d6b76;
    --ink-soft: #7a8892;
    --rule: #e3e6ea;
    --chip: #eef1f4;
    --blue-link: #3b6fd8;
    --blue-deep: #2f63e6;
    --blue-pale: #dbe6fa;
    --brand: #5a6b75;
  }
  * { margin: 0; padding: 0; box-sizing: border-box; }
  html, body { width: 1200px; height: 849px; overflow: hidden; background: var(--page); }
  .sheet { position: relative; width: 1200px; height: 849px; font-family: "Bitter", Georgia, serif; }

  .headline { position: absolute; left: 326px; top: 148px; color: var(--ink-dark); font-style: italic; }
  .headline__main { font-weight: 700; font-size: 17px; line-height: 22px; }
  .headline__sub { font-weight: 400; font-size: 16px; line-height: 22px; }

  .lead { position: absolute; left: 326px; top: 212px; width: 545px; color: var(--ink-mid);
          font-style: italic; font-size: 16px; line-height: 23px; }

  .trends { position: absolute; left: 326px; top: 274px; width: 543px; height: 226px;
            font-family: "Roboto", Arial, sans-serif; }
  .trends__divider { position: absolute; left: 273px; top: 0; width: 1px; height: 226px; background: var(--rule); }
  .trends__label { position: absolute; font-size: 9.5px; font-weight: 500; color: #333; }
  .trends__crumb { position: absolute; left: 0; top: 25px; font-size: 8px; color: #555; }
  .trends__toggle { position: absolute; display: flex; border: 1px solid var(--rule); height: 19px; }
  .trends__toggle span { display: flex; align-items: center; justify-content: center; font-size: 8px; color: #555; }
  .trends__toggle .is-active { background: var(--chip); }
  .trends__map { position: absolute; left: 46px; top: 42px; width: 190px; height: 148px;
                 background: linear-gradient(90deg, var(--blue-pale) 0%, var(--blue-pale) 50%, #6f95ee 62%, var(--blue-deep) 80%);
                 border-radius: 40% 45% 35% 40%; }
  .trends__legend { position: absolute; left: 0; top: 209px; display: flex; align-items: center; gap: 6px;
                    font-size: 7px; color: #333; }
  .trends__legend-bar { width: 62px; height: 6px; background: linear-gradient(90deg, #ffffff, var(--blue-deep)); }
  .trends__scope { position: absolute; right: 279px; top: 208px; font-size: 7.5px; color: var(--blue-link); }
  .trends__term { position: absolute; left: 290px; top: 42px; font-size: 8px; color: var(--blue-link); }
  .trends__change { position: absolute; right: 0; top: 42px; font-size: 8px; color: #555; }

  .source { position: absolute; left: 326px; top: 508px; color: var(--ink-soft); font-style: italic; font-size: 12px; }
  .source strong { font-weight: 700; }

  .quote { position: absolute; left: 326px; top: 545px; width: 545px; color: var(--ink-soft);
           font-style: italic; font-size: 14.6px; line-height: 20.3px; text-align: justify; hyphens: auto; }

  .brand { position: absolute; left: 994px; top: 736px; display: flex; align-items: flex-end; gap: 3px;
           color: var(--brand); font-family: "Bitter", Georgia, serif; font-weight: 700; font-size: 29px; line-height: 1; letter-spacing: -0.5px; }
  .brand__dot { width: 6px; height: 6px; border-radius: 50%; background: var(--brand); margin-bottom: 3px; }
</style>
</head>
<body>
<main class="sheet">
  <header class="headline">
    <h1 class="headline__main">The Aluminium</h1>
    <h2 class="headline__sub">Free Deodorant Trend</h2>
  </header>

  <p class="lead">Searchly search interest for aluminium free deodorant increases 60% in Australia</p>

  <section class="trends" aria-label="Search interest panel">
    <span class="trends__label" style="left:0;top:4px;">Regional interest</span>
    <span class="trends__crumb">Worldwide › Australia</span>
    <div class="trends__toggle" style="left:197px;top:0;">
      <span class="is-active" style="width:36px;">
        <svg width="10" height="10" viewBox="0 0 10 10"><circle cx="5" cy="5" r="4.2" fill="none" stroke="#333" stroke-width="1.2"/><path d="M1 5h8M5 1c-2 2-2 6 0 8M5 1c2 2 2 6 0 8" fill="none" stroke="#333" stroke-width="0.9"/></svg>
      </span>
      <span style="width:36px;">
        <svg width="9" height="7" viewBox="0 0 9 7"><path d="M0 1h9M0 3.5h9M0 6h9" stroke="#777" stroke-width="1"/></svg>
      </span>
    </div>
    <div class="trends__map" role="img" aria-label="Map of Australia shaded by search interest, strongest in the eastern states"></div>
    <div class="trends__legend"><span>0</span><span class="trends__legend-bar"></span><span>100</span></div>
    <span class="trends__scope">Subregion | City</span>

    <div class="trends__divider"></div>

    <span class="trends__label" style="left:290px;top:4px;">Related terms</span>
    <div class="trends__toggle" style="left:443px;top:0;">
      <span style="width:50px;">Top</span>
      <span class="is-active" style="width:50px;">Rising</span>
    </div>
    <span class="trends__term">aluminium free deodorant</span>
    <span class="trends__change">+60%</span>
  </section>

  <p class="source"><strong>Source:</strong> Searchly Trends 2013</p>

  <blockquote class="quote">‘Despite Oncology Trust UK issuing a statement saying that “there is no convincing evidence that antiperspirants and deodorants cause breast cancer,” ongoing consumer concern means that sales of previously niche aluminium-free deodorant brands such as Juniper and Willow’s of Vermont are growing, and are increasingly being sold in mainstream retail outlets such as Harrowgate in the UK. As these natural, free-from aluminium deodorants typically retail at around twice the price of their standard counterparts, the natural segment will be an increasingly important area of growth going forward.’ (Marketscope 2009).</blockquote>

  <div class="brand"><span>velora</span><span class="brand__dot"></span></div>
</main>
</body>
</html>
```